Health Coach needs a Business Card Design

Need a really modern feminine business card design for a health and lifestyle coach. Needs to use geometric shapes, muted grey/blue/green pastels and black and white - see mood board attached and logo. The client likes black and white, modern, san serif with the use of lines and possibly a shadow leaf as in the mood board. Possibly put the tag line on the back or an icon of the logo. Logo is also attached. An icon of the logo would be great too.

Target Market(s)

Women (some men) aged 30 to 50.

Industry/Entity Type

Business

Contact Information for Business Card

Marla Teveny
e-mail: hello@marlatwell.example
website: marlatwell.example
Phone: +610497258316

The tag line is "Steady habits, lasting ease"

Font styles to use
Sans Serif

Colors
ecf7fb
cfeae6
000000
ffffff
f5f5f5

Requirements
Must have
• Black and white, logo, tag line and details
Nice to have
• Would be nice to incorporate the shadow palm.fern leaves as in the mood board and or geometric lines/shapes - see mood board. Could be either standard rectangle or would be happy with square too.
Should not have
• Flowers or decorations

```html
<!DOCTYPE html>
<html lang="en">
<head>
<meta charset="utf-8">
<title>Marla Teveny — Business Card</title>
<link rel="stylesheet" href="https://fonts.googleapis.com/css2?family=Questrial&display=swap">
<style>
  :root {
    --backdrop: #e4e7e9;
    --card: #ffffff;
    --ink: #555555;
    --ink-soft: #777777;
    --mint: #cfeae6;
    --mint-pale: #ecf7fb;
    --frame: #dcefeb;
  }
  * { margin: 0; padding: 0; box-sizing: border-box; }
  html, body {
    width: 1200px;
    height: 794px;
    overflow: hidden;
    background: var(--backdrop);
    font-family: "Questrial", sans-serif;
    color: var(--ink);
  }
  .canvas { position: relative; width: 1200px; height: 794px; }
  .card {
    position: absolute;
    background: var(--card);
    overflow: hidden;
    box-shadow: 0 2px 10px rgba(0,0,0,0.08);
  }

  /* Front: contact details */
  .card--front { left: 613px; top: 79px; width: 480px; height: 294px; }
  .front__foliage {
    position: absolute;
    right: 0; top: 0;
    width: 220px; height: 215px;
    background: radial-gradient(ellipse at 70% 40%, var(--mint) 0%, rgba(207,234,230,0.5) 45%, rgba(255,255,255,0) 75%);
  }
  .contact { position: absolute; left: 42px; top: 150px; }
  .contact__name {
    font-size: 16px;
    letter-spacing: 1.4px;
    text-transform: uppercase;
    font-weight: 400;
    margin-bottom: 5px;
  }
  .contact__line { font-size: 12.5px; line-height: 20px; }
  .contact__web {
    position: absolute;
    left: 42px; top: 238px;
    font-size: 13px;
    letter-spacing: 1.6px;
    text-transform: uppercase;
  }

  /* Back: brand name and tag line */
  .card--back { left: 101px; top: 404px; width: 477px; height: 293px; }
  .back__foliage {
    position: absolute;
    left: 0; width: 100%; height: 74px;
    background: linear-gradient(90deg, var(--mint-pale), var(--mint) 50%, var(--mint-pale));
    opacity: 0.8;
  }
  .back__foliage--top { top: 0; }
  .back__foliage--bottom { bottom: 0; height: 72px; }
  .brand-frame {
    position: absolute;
    left: 42px; top: 87px;
    width: 395px; height: 120px;
    border: 2px solid var(--frame);
    text-align: center;
  }
  .brand-frame__name {
    margin-top: 30px;
    font-size: 30px;
    line-height: 32px;
    letter-spacing: 1.5px;
    color: var(--ink-soft);
    font-weight: 400;
  }
  .brand-frame__tagline {
    margin-top: 12px;
    font-size: 12.5px;
    letter-spacing: 2.6px;
    text-transform: uppercase;
    color: var(--ink-soft);
  }
</style>
</head>
<body>
  <main class="canvas">
    <section class="card card--front">
      <div class="front__foliage" role="img" aria-label="Pale mint fern leaf illustration"></div>
      <div class="contact">
        <h1 class="contact__name">Marla Teveny</h1>
        <p class="contact__line">hello@marlatwell.example</p>
        <p class="contact__line">+610497258316</p>
      </div>
      <p class="contact__web">marlatwell.example</p>
    </section>

    <section class="card card--back">
      <div class="back__foliage back__foliage--top" role="img" aria-label="Band of pale mint fern leaf pattern"></div>
      <div class="brand-frame">
        <p class="brand-frame__name">Teveny Wellness</p>
        <p class="brand-frame__tagline">Steady habits, lasting ease</p>
      </div>
      <div class="back__foliage back__foliage--bottom" role="img" aria-label="Band of pale mint fern leaf pattern"></div>
    </section>
  </main>
</body>
</html>
```